hollowmere crest website

We need a new website for our new business division. We are a sustainable design firm specializing in servicing the needs if architects and developers. We have a staff consisting of architects, engineers, and former contractors and we understand green must make sense.

Bottomline - the only sustainable and hollowmere crest solutions are those thatbare good for the environment and good for our clients bottom line.

Our company is hollowmere crest and we will send you a copy of our logo you will see our tagline. Is simple. sustainable. solutions. The play with the periods is that we believe their are simple sustainable solutions and we want to use the words together and possible let each stand alone to accentuate their individual meaning in regards to benefit to our clients.

We want a cool splash page with nich graphics and pictures then later pages to feature projects and design ideas.

Target Market(s)

Our target customers are architects, developers, and contractors who would need assistance with the design process for a OVRA project or assisatnce with a building owner who wants to make tehir facilty more environmentally friendly and save energy costs at the same tiem.

Industry/Entity Type

Environment

Requirements
Must have
• Needs a construction look with an environmentally friendly surrounding that is pleasing to look at. Must appeal to the client not only as environmentally friendly but also a wise investment.
Nice to have
• Opportunity for a connection to Social networking including a blog.
Should not have
• A totally environmental building feel at whatever cost. We want to emphasize that it is possible to build environmental friendly and save you money over the life of your building

```html
<!DOCTYPE html>
<html lang="en">
<head>
<meta charset="utf-8">
<title>hollowmere crest — simple. sustainable. solutions.</title>
<link rel="stylesheet" href="https://fonts.googleapis.com/css2?family=Anton&family=Comfortaa:wght@400;700&family=Arimo:wght@400;700&display=swap">
<style>
  :root {
    --green: #3fae2a;
    --green-dark: #2f8f1e;
    --leaf: #5cc23a;
    --grey-dark: #3d3d3d;
    --ink: #222222;
    --rule: #c8c8c8;
    --paper: #ffffff;
    --feed: #f08a24;
    --social-a: #3fa9e0;
    --social-b: #3b5da8;
  }
  * { box-sizing: border-box; }
  html, body {
    margin: 0;
    width: 1200px;
    height: 900px;
    overflow: hidden;
    background: var(--paper);
  }
  .page {
    position: relative;
    width: 1200px;
    height: 900px;
  }
  .site-nav {
    position: absolute;
    top: 0; left: 0;
    width: 1200px;
    height: 132px;
    background: linear-gradient(180deg, var(--leaf), var(--green) 60%, var(--green-dark));
  }
  .nav-tile {
    position: absolute;
    top: 0;
    height: 126px;
    border-radius: 0 0 14px 14px;
    display: flex;
    align-items: center;
    justify-content: center;
    color: #ffffff;
    font-family: "Comfortaa", sans-serif;
    font-weight: 700;
    font-size: 28px;
    text-decoration: none;
    padding-bottom: 6px;
  }
  .nav-tile--home { left: 0; width: 240px; background: none; }
  .nav-tile--blog { left: 242px; width: 238px; background: linear-gradient(160deg, #6b6b6b, #2e2e2e 55%, #8c8c8c); }
  .nav-tile--smart { left: 484px; width: 236px; background: linear-gradient(170deg, #9a9a9a, #4a4a4a 50%, #1f1f1f); }
  .nav-tile--green { left: 724px; width: 236px; background: linear-gradient(180deg, #5a5a5a, #2a2a2a 60%, #444); }
  .nav-tile--projects { left: 968px; width: 232px; background: linear-gradient(150deg, #7d7d7d, #3a3a3a 50%, #9a9a9a); }
  .nav-tile span { position: relative; }

  .headline {
    position: absolute;
    top: 220px;
    left: 236px;
    width: 724px;
    height: 400px;
    overflow: visible;
  }
  .headline text {
    font-family: "Anton", sans-serif;
  }

  .intro {
    position: absolute;
    left: 240px;
    top: 642px;
    width: 390px;
    margin: 0;
    font-family: "Arimo", sans-serif;
    font-size: 11px;
    line-height: 14px;
    color: var(--ink);
  }
  .brand {
    position: absolute;
    left: 680px;
    top: 644px;
    width: 276px;
    display: flex;
    align-items: center;
    gap: 8px;
    font-family: "Arimo", sans-serif;
  }
  .brand-mark {
    width: 48px; height: 48px;
    background: var(--green);
    flex: none;
  }
  .brand-name {
    font-size: 27px;
    font-weight: 400;
    color: var(--grey-dark);
    line-height: 1;
    letter-spacing: -0.5px;
    white-space: nowrap;
  }
  .brand-tagline {
    font-size: 11.5px;
    color: var(--green-dark);
    margin-top: 4px;
    white-space: nowrap;
  }
  .divider {
    position: absolute;
    left: 240px;
    top: 716px;
    width: 716px;
    height: 1px;
    background: var(--rule);
  }
  .social {
    position: absolute;
    top: 728px;
    left: 854px;
    display: flex;
    gap: 8px;
  }
  .social a {
    display: block;
    width: 28px; height: 28px;
    border-radius: 6px;
  }
  .social .feed { background: var(--feed); }
  .social .net-a { background: var(--social-a); }
  .social .net-b { background: var(--social-b); }
  .copyright {
    position: absolute;
    left: 240px;
    top: 866px;
    margin: 0;
    font-family: "Arimo", sans-serif;
    font-size: 10px;
    color: var(--ink);
  }
</style>
</head>
<body>
<div class="page">
  <nav class="site-nav">
    <a class="nav-tile nav-tile--home" href="#"><span>home</span></a>
    <a class="nav-tile nav-tile--blog" href="#" role="img" aria-label="blog — photo of a modern curved office building"><span>blog</span></a>
    <a class="nav-tile nav-tile--smart" href="#" role="img" aria-label="smart — photo of a sweeping glass roof"><span>smart</span></a>
    <a class="nav-tile nav-tile--green" href="#" role="img" aria-label="green — photo of a building facade"><span>green</span></a>
    <a class="nav-tile nav-tile--projects" href="#" role="img" aria-label="projects — photo of a lattice glass tower"><span>projects</span></a>
  </nav>

  <svg class="headline" viewBox="0 0 724 400" role="img" aria-label="Simple. Sustainable. Solutions. — lettering filled with a city skyline fading into green leaves">
    <defs>
      <linearGradient id="fill-simple" x1="0" y1="0" x2="1" y2="1">
        <stop offset="0" stop-color="#d6d6d6"/>
        <stop offset="0.6" stop-color="#9a9a9a"/>
        <stop offset="1" stop-color="#6e6e6e"/>
      </linearGradient>
      <linearGradient id="fill-sustainable" x1="0" y1="0" x2="1" y2="0">
        <stop offset="0" stop-color="#2f2f2f"/>
        <stop offset="0.5" stop-color="#4a4a4a"/>
        <stop offset="0.75" stop-color="#5c9a3a"/>
        <stop offset="1" stop-color="#49b52c"/>
      </linearGradient>
      <linearGradient id="fill-solutions" x1="0" y1="0" x2="1" y2="0">
        <stop offset="0" stop-color="#6a6a6a"/>
        <stop offset="0.3" stop-color="#555555"/>
        <stop offset="0.55" stop-color="#4f8f34"/>
        <stop offset="1" stop-color="#3fae2a"/>
      </linearGradient>
    </defs>
    <text x="4" y="164" font-size="186" textLength="716" lengthAdjust="spacingAndGlyphs" fill="url(#fill-simple)">SIMPLE.</text>
    <text x="4" y="266" font-size="100" textLength="716" lengthAdjust="spacingAndGlyphs" fill="url(#fill-sustainable)">SUSTAINABLE.</text>
    <text x="4" y="390" font-size="128" textLength="716" lengthAdjust="spacingAndGlyphs" fill="url(#fill-solutions)">SOLUTIONS.</text>
  </svg>

  <p class="intro">Lorem Ipsum is simply dummy text of the printing and typesetting industry. Lorem Ipsum has been the industry's standard dummy text ever since the 1500s, when an unknown printer took a galley of type and scrambled it to make a type specimen book.</p>

  <div class="brand">
    <div class="brand-mark"></div>
    <div>
      <div class="brand-name">hollowmere crest</div>
      <div class="brand-tagline">simple. sustainable. solutions.</div>
    </div>
  </div>

  <div class="divider"></div>

  <div class="social">
    <a class="feed" href="#" aria-label="news feed"></a>
    <a class="net-a" href="#" aria-label="social network"></a>
    <a class="net-b" href="#" aria-label="social network"></a>
  </div>

  <p class="copyright">Copyright © 2011 hollowmerecrest.</p>
</div>
</body>
</html>
```